Cards & Invitations

Hi!
We would like you to design 3 amazing cards for us.
1. Wedding invitation.
We would like to have a spring wedding invitation. It has to be A4 folded to A5 format, floral theme, but made in a very classic style. It has to contain light green and blue colors, but you are free to use other colors as well.
Text to be included:
Mr. and Mrs. Delwyn Avercross
Request the honour of your presence
At the marriage of their daughter
Marisse Avercross
to
Owen Ralditch
Saturday, the eighteenth of April
Two thousand and twelve
At three o'clock in the afternoon
Saint Wendel's Church
58 Brindle Street,
South Hampton, New York
Followed by a dinner at
Restaurant Verlane, Osgood Road 347
R.S.V.P. by the ninth of April
2. Christening invitation in Vintage style.
We need an invitation for a christening of Nico Farrowby. We would like it to be in vintage style, in light pink or lilac color and containing the photo of the baby.
It should also have some church symbols, like cross, prayer beads etc (one element is enough, not all together). Format: A5 horisontal (landscape) card. Please, find the photo attached.
Text to be included:
You are invited to
Witness and Celebrate
the Baptism of our daughter
Nico Farrowby
Sunday, September 26th at 1 p.m.
St. Ambrel Church
5821 Lindqvist Row, Parktown
Reception following the ceremony
at the Farrowby home
7302 Harlowe, Pearl Sound
Please reply by September 18th
3. Birthday invitation.
This is an invitation for Nico's 7th birthday party. The theme is racing. It should contain his photo and a race car (cars) or racing competition. No color preferences. It's a square folded card. Please, find attached the photo.
Text on the outside: Nico is turning 7
Text on the inside:
You are invited to join us
for Nico's 7th Birthday Celebration
Saturday, September 18th
We will have the celebration at Blue Juniper,
486 Quillby Road, Federal Way
Please reply by September 7th
to Bram at 175-389-602
Welcome!

```html
<!DOCTYPE html>
<html lang="en">
<head>
<meta charset="utf-8">
<title>Christening Invitation – Nico Farrowby</title>
<link rel="stylesheet" href="https://fonts.googleapis.com/css2?family=Courgette&family=Merienda:wght@700&family=Kaushan+Script&display=swap">
<style>
  :root {
    --backdrop: #efe9e2;
    --card-white: #ffffff;
    --lilac-band: #eab8ec;
    --lilac-soft: #f4cdf3;
    --envelope-pink: #fcdcf8;
    --ink-brown: #8a5316;
    --photo-light: #f3d6cc;
    --photo-mid: #e7b3a8;
    --photo-deep: #cf8f8c;
    --cross-white: #fdf6fd;
  }
  * { box-sizing: border-box; margin: 0; padding: 0; }
  html, body { width: 1200px; height: 1080px; overflow: hidden; background: var(--backdrop); }
  .canvas { position: relative; width: 1200px; height: 1080px; }

  .invitation-card {
    position: absolute; left: 125px; top: 130px; width: 901px; height: 384px;
    background: var(--card-white);
    box-shadow: 0 3px 8px rgba(0,0,0,.25);
    overflow: hidden;
  }
  .baby-photo {
    position: absolute;
    background: radial-gradient(ellipse at 55% 60%, var(--photo-light) 0%, var(--photo-mid) 55%, var(--photo-deep) 100%);
  }
  .invitation-card .baby-photo { left: 0; top: 0; width: 323px; height: 384px; }
  .lace-band {
    position: absolute;
    background: linear-gradient(90deg, var(--lilac-band), var(--lilac-soft), var(--lilac-band));
  }
  .invitation-card .lace-band { left: 323px; top: 0; width: 118px; height: 384px; }
  .cross-badge { position: absolute; left: 784px; top: 10px; width: 104px; height: 104px; }
  .invitation-text {
    position: absolute; left: 461px; width: 368px; top: 57px;
    text-align: center;
    font-family: "Courgette", cursive;
    font-size: 18px; line-height: 24px;
    color: var(--ink-brown);
    white-space: nowrap;
  }
  .phone-line {
    position: absolute; left: 461px; width: 368px; top: 344px;
    text-align: center;
    font-family: "Merienda", cursive; font-weight: 700;
    font-size: 21px; line-height: 30px; letter-spacing: 1px;
    color: var(--ink-brown);
  }

  .envelope {
    position: absolute; left: 125px; top: 538px; width: 901px; height: 381px;
    background: var(--envelope-pink);
    box-shadow: 0 3px 8px rgba(0,0,0,.25);
    overflow: hidden;
  }
  .envelope .lace-band { left: 0; top: 151px; width: 901px; height: 74px; }
  .photo-frame {
    position: absolute; left: 74px; top: 32px; width: 441px; height: 330px;
    background: var(--card-white); padding: 6px;
  }
  .photo-frame .baby-photo { position: static; width: 100%; height: 100%; }
  .envelope-title {
    position: absolute;
    font-family: "Kaushan Script", cursive;
    font-weight: 400;
    font-size: 36px; line-height: 40px;
    color: var(--ink-brown);
    white-space: nowrap;
  }
  .title-baptism { left: 557px; top: 98px; }
  .title-daughter { left: 678px; top: 175px; }
  .title-name { left: 542px; top: 241px; }
</style>
</head>
<body>
<main class="canvas">

  <section class="invitation-card">
    <div class="baby-photo" role="img" aria-label="Photo of the sleeping baby in a pink knitted hat"></div>
    <div class="lace-band" role="img" aria-label="Lilac vintage lace pattern band"></div>

    <svg class="cross-badge" viewBox="0 0 104 104" aria-hidden="true">
      <circle cx="52" cy="52" r="52" fill="var(--lilac-band)"/>
      <path d="M47 14 h10 v22 h18 v9 h-18 v45 h-10 v-45 h-18 v-9 h18 z" fill="var(--cross-white)"/>
    </svg>

    <div class="invitation-text">
      <p>You are invited to</p>
      <p>Witness and Celebrate</p>
      <p>the Baptism of our daughter</p>
      <p>Nico Farrowby</p>
      <p>Sunday, September 26th at 1 p.m.</p>
      <p>St. Ambrel Church</p>
      <p>5821 Lindqvist Row, Parktown</p>
      <p>Reception following the ceremony</p>
      <p>at the Farrowby home</p>
      <p>7302 Harlowe, Pearl Sound</p>
      <p>Please reply by September 18th</p>
    </div>
    <div class="phone-line">Tel no 00000000</div>
  </section>

  <section class="envelope">
    <div class="lace-band" role="img" aria-label="Lilac vintage lace pattern band"></div>
    <div class="photo-frame">
      <div class="baby-photo" role="img" aria-label="Close-up photo of the sleeping baby"></div>
    </div>
    <h1 class="envelope-title title-baptism">Baptism of</h1>
    <h2 class="envelope-title title-daughter">our daughter</h2>
    <h2 class="envelope-title title-name">Nico Farrowby</h2>
  </section>

</main>
</body>
</html>
```